Kessler MD Summit Primary Care Business Card

Need a business card for a medical clinic targeting VIP patients. Should portray an upscale feeling. Simple, clean design. Logo and colors need to be incorporated into card. Clinic colors are gray/ silver, blues, white same as logo.
Clinic is a cash only VIP service clinic targeting higher income patients.
Tagline: "Personal care, unhurried time - every single visit"

Target Market(s)

VIP, upscale

Industry/Entity Type

Medical

Contact Information for Business Card

Would like to use for cards with raised print or metallic highlight.

Requirements
Must have
• Incorporate logo, Use colors in logo
Nice to have
• Metallic detail
Should not have
• too much details or colors, other stock photos or designs

```html
<!DOCTYPE html>
<html lang="en">
<head>
<meta charset="UTF-8">
<title>Kessler MD Summit Primary Care – Business Card</title>
<link rel="stylesheet" href="https://fonts.googleapis.com/css2?family=Lato:wght@400;700;900&display=swap">
<style>
  :root {
    --navy: #1f3a63;
    --slate: #93a3b5;
    --mist: #cdd4df;
    --paper: #fafcfd;
    --backdrop: #e8ecef;
    --white: #ffffff;
  }
  * { margin: 0; padding: 0; box-sizing: border-box; }
  html, body {
    width: 1200px;
    height: 1200px;
    overflow: hidden;
    background: var(--backdrop);
    font-family: "Lato", Arial, sans-serif;
  }
  .business-card {
    position: absolute;
    left: 60px;
    top: 322px;
    width: 1080px;
    height: 556px;
    background: var(--paper);
    box-shadow: 0 6px 22px rgba(20, 35, 60, 0.18);
    overflow: hidden;
  }
  .card-shapes {
    position: absolute;
    inset: 0;
    width: 100%;
    height: 100%;
  }
  .tagline {
    position: absolute;
    top: 47px;
    left: 0;
    width: 100%;
    text-align: center;
    font-size: 28px;
    font-weight: 700;
    color: var(--navy);
  }
  .clinic-mark {
    position: absolute;
    top: 198px;
    left: 488px;
    width: 100px;
    height: 100px;
    border-radius: 50%;
    background: var(--navy);
  }
  .clinic-name {
    position: absolute;
    top: 346px;
    left: 0;
    width: 100%;
    text-align: center;
    color: var(--navy);
    font-weight: 700;
    text-transform: uppercase;
    line-height: 1.15;
  }
  .clinic-name .name-line-top { display: block; font-size: 36px; letter-spacing: 3px; }
  .clinic-name .name-line-bottom { display: block; font-size: 38px; letter-spacing: 2px; }
  .contact {
    position: absolute;
    left: 42px;
    display: flex;
    align-items: center;
    gap: 14px;
    font-size: 24px;
    font-weight: 400;
  }
  .contact svg { width: 30px; height: 30px; flex: none; }
  .contact-phone { top: 398px; color: var(--navy); }
  .contact-email { top: 491px; color: var(--white); }
</style>
</head>
<body>
  <div class="business-card">
    <svg class="card-shapes" viewBox="0 0 798 411" preserveAspectRatio="none" aria-hidden="true">
      <polygon points="600,0 708,0 798,66" fill="var(--mist)"/>
      <polygon points="708,0 798,0 798,66" fill="var(--navy)"/>
      <polygon points="0,323 798,411 0,411" fill="var(--navy)"/>
      <polygon points="526,381 798,343 798,411" fill="var(--slate)"/>
    </svg>

    <p class="tagline">"Personal care, unhurried time - every single visit"</p>

    <div class="clinic-mark"></div>
    <h1 class="clinic-name">
      <span class="name-line-top">Kessler MD</span>
      <span class="name-line-bottom">Summit Primary Care</span>
    </h1>

    <div class="contact contact-phone">
      <svg viewBox="0 0 24 24" aria-hidden="true"><path fill="currentColor" d="M6.6 10.8c1.4 2.8 3.8 5.1 6.6 6.6l2.2-2.2c.3-.3.7-.4 1-.2 1.1.4 2.3.6 3.6.6.6 0 1 .4 1 1V20c0 .6-.4 1-1 1C10.6 21 3 13.4 3 4c0-.6.4-1 1-1h3.5c.6 0 1 .4 1 1 0 1.3.2 2.5.6 3.6.1.3 0 .7-.2 1L6.6 10.8z"/></svg>
      <span>(000)00000</span>
    </div>

    <div class="contact contact-email">
      <svg viewBox="0 0 24 24" aria-hidden="true">
        <rect x="2" y="5" width="20" height="14" fill="currentColor"/>
        <polyline points="2.5,5.5 12,12.5 21.5,5.5" fill="none" stroke="var(--navy)" stroke-width="1.8" stroke-linejoin="round"/>
      </svg>
      <span>mail@mail.com</span>
    </div>
  </div>
</body>
</html>
```